need a Flyer for Plush Toy company

Need a Flyer for Plush Toy company ,

I upload a file for TEXT

Target Market(s)

Toys wholesalers , Supermarket

Industry/Entity Type

Toy Store

Colors
000000
ec1f27
c4c4c4

Requirements
Must have
• I have up loaded 3 files
• 1. Logo Registered Brand
• 2. customer's design in drawing
• 3. our ready samples based on Design
Nice to have
• happy kids in Nature ,
• happy kids in Ski ,
• different color Kids ,
• Multi culture concept

```html
<!DOCTYPE html>
<html lang="en">
<head>
<meta charset="utf-8">
<title>Harbor Plush – Innovative Developer for Plush Toys</title>
<link rel="stylesheet" href="https://fonts.googleapis.com/css2?family=Arimo:wght@400;700&family=PT+Sans+Narrow:wght@700&display=swap">
<style>
  :root {
    --black: #000000;
    --red: #ec1f27;
    --grey: #c4c4c4;
    --white: #ffffff;
    --meadow-top: #8fc6e8;
    --meadow-mid: #9ccf4a;
    --meadow-low: #5f9a22;
  }
  * { box-sizing: border-box; margin: 0; padding: 0; }
  html, body { width: 1200px; height: 1200px; overflow: hidden; background: var(--white); }
  body { font-family: "Arimo", Arial, sans-serif; }

  .flyer {
    position: absolute; left: 177px; top: 0;
    width: 846px; height: 1200px;
    background: var(--red); color: var(--white);
  }

  .hero { position: absolute; left: 0; top: 0; width: 846px; height: 332px; display: flex; }
  .brand-panel {
    width: 370px; height: 332px; background: var(--black);
    display: flex; align-items: center; justify-content: center; gap: 14px;
  }
  .brand-mark { width: 34px; height: 34px; border-radius: 50%; background: var(--red); }
  .brand-name { font-weight: 700; font-size: 34px; color: var(--white); letter-spacing: 0.5px; }
  .kids-photo {
    width: 476px; height: 332px;
    background: linear-gradient(180deg, var(--meadow-top) 0%, #b9dca0 30%, var(--meadow-mid) 55%, var(--meadow-low) 100%);
  }

  .headline {
    position: absolute; left: 0; top: 356px; width: 846px; text-align: center;
    font-family: "PT Sans Narrow", "Arial Narrow", sans-serif; font-weight: 700;
    font-size: 56px; letter-spacing: 0.5px;
    text-shadow: 3px 4px 5px rgba(0,0,0,0.75);
  }

  .intro, .offer {
    position: absolute; font-size: 20.5px; line-height: 36px; text-align: justify;
  }
  .intro { left: 36px; top: 450px; width: 774px; }
  .offer { left: 422px; top: 658px; width: 388px; }

  .plush-samples {
    position: absolute; left: 0; top: 696px; width: 412px; height: 152px;
    background: radial-gradient(ellipse at 50% 55%, #f6e37a 0%, #d9c6e8 40%, rgba(236,31,39,0) 72%);
  }

  .contact-band {
    position: absolute; left: 0; top: 922px; width: 846px; height: 278px;
    background: var(--black);
  }
  .company {
    position: absolute; left: 41px; top: 28px; font-size: 21px; line-height: 32px;
  }
  .company-name { font-weight: 700; font-size: 26px; margin-bottom: 2px; }
  .bank {
    position: absolute; left: 457px; top: 120px; font-size: 21px; line-height: 32px;
  }
</style>
</head>
<body>
  <main class="flyer">
    <section class="hero">
      <div class="brand-panel">
        <span class="brand-mark"></span>
        <span class="brand-name">Harbor Plush</span>
      </div>
      <div class="kids-photo" role="img" aria-label="Photo of happy children of different backgrounds running hand in hand across a sunny flower meadow"></div>
    </section>

    <h1 class="headline">Innovative Developer&nbsp; for Plush Toys</h1>

    <p class="intro">We live and work in Falkenfeld near to Cologne Germany. We speak German and English. The toys are made in China, we are small family business , but we are professional in Plush toys business , right now we have successfully launched Projects with a huge Japanese 100 Yen Chain Store.&nbsp; Here in Flyer we show a Sample project.</p>

    <div class="plush-samples" role="img" aria-label="Row of small sample plush toys: pink bunny, white bird, lion, purple and blue creatures and a yellow chick"></div>

    <p class="offer">100 Yen = 0.90 USD&nbsp;&nbsp;, Our products can meet strictest Quality Control , but are with extremely Low Price to fit for&nbsp; Japanese Dollar Shop as well as his overseas Store around the world. Of course our products are fit for&nbsp; Premium Store too.</p>

    <footer class="contact-band">
      <div class="company">
        <div class="company-name">LENA HARTWIG, FAMILY BUSINESS</div>
        <div>LINDENSTRASSE 8, 50999 FALKENFELD GERMANY</div>
        <div>lena@harborplush.de</div>
        <div>Fon&nbsp;&nbsp; +49 (0)&nbsp; 2200- 555 0142</div>
        <div>Fax&nbsp;&nbsp; +49 (0)&nbsp; 2200- 555 0143</div>
        <div>Mobil:&nbsp; +49 (0) 170 5550 198</div>
        <div>Ust-IdNr./VAT No. DE123456789</div>
      </div>
      <div class="bank">
        <div>BANK INFORMATION :</div>
        <div>ACCOUNT HOLDER:&nbsp;&nbsp; MARA KESSLER</div>
        <div>IBAN:&nbsp; DE00 1234 5678 9012 3456 78</div>
        <div>BIC : ABCDDEFF000</div>
      </div>
    </footer>
  </main>
</body>
</html>
```